Web Design For Coral Basin Pool Service

We are working with a company that wants a website for their pool service. Some sites to use for content/competitors and inspiration:
https://sacramento.lumawaterworks.example/builder/newbuild/repair/ppc
https://orchardsplashcareplus.example/
https://bluefinaquacare.example/
https://www.halvorsenplasterworks.example/pool-renovation-ga/
Thank you for taking the time to consider designing a website for us. We are web developers based in Stockton, CA, USA. Most of our projects go through the same process. Understanding this process may help you win a project with us. We custom-code all of our websites in-house. We don’t have any requirements as to what tools you use for your design, but we prefer Figma files. For any design that we label as four-stars, we send it to the client for review. The client picks the final design they want us to use. Once we complete this process, we will continue to show additional clients all the four-star sites and purchase them later. Your designs will have multiple chances to sell. For better chances of success, we ask that you follow these guidelines.
IMAGES:
If you use any images or icons in the design, we ask that you have a link to the asset so we can purchase the image/icon. Most of the designs we submit do not have the customer’s images on them unless they have some great images. Be creative; show us the feeling you are trying to portray with your image choices. Use any royalty-free site you choose. We subscribe to Adobe and mainly use their images, but we can purchase images outside of Adobe. PLEASE NOTE: we will not submit designs to clients with watermarks on the images.
FONTS:
We ask that you identify the fonts used in the design. This can be done in a message if you want. We typically use Google Fonts and Adobe Fonts.
CONTENT:
We're always open to different content and ideas. We often submit designs with stock images so the client can see our vision. We typically take pictures after the website launch to use their images with our vision. Lorem Ipsum is fine for paragraphs, but we ask that you write the headers in correct English. We want to be able to show the vision and identify the sections of the website.
INSPIRATION:
We typically add a couple of links in the brief of websites we like to help you get started in your design.
REVISIONS:
We do not often ask for revisions of the designs unless we see something in the design that may not appeal to the client. If there are slight changes that we want to make, we do that in the development process.
FEEDBACK:
We rarely give feedback on designs during the design process. We are working on many website projects and do not have the time to provide feedback. We usually respond if your request is well thought out and asks specific questions, but a note asking “feedback, please” usually goes unanswered.

```html
<!DOCTYPE html>
<html lang="en">
<head>
<meta charset="utf-8">
<title>Coral Basin Pool Service</title>
<link rel="stylesheet" href="https://fonts.googleapis.com/css2?family=Marcellus&family=Questrial&display=swap">
<style>
:root{
  --blue:#2a8fe6;
  --blue-deep:#1464c8;
  --blue-dark:#0d3f86;
  --sky:#e9f4fd;
  --ink:#2b2b2b;
  --muted:#555c66;
  --white:#ffffff;
  --water:#5fc3ee;
  --heading:"Marcellus", Georgia, serif;
  --body:"Questrial", Arial, sans-serif;
}
*{box-sizing:border-box;margin:0;padding:0}
html,body{width:1200px;height:5064px;overflow:hidden}
body{font-family:var(--body);color:var(--ink);background:var(--white);position:relative}
.section{position:absolute;left:0;width:1200px}
p{font-size:16px;line-height:1.7;color:var(--muted)}
.btn{display:inline-block;background:var(--blue);color:var(--white);font-family:var(--body);font-size:15px;letter-spacing:1px;border-radius:30px;padding:12px 30px;text-transform:uppercase}
.heading{font-family:var(--heading);font-size:56px;letter-spacing:2px;text-transform:uppercase;font-weight:400}
.heading .accent{color:var(--blue)}

/* header & hero */
.hero{top:0;height:760px}
.hero-photo{position:absolute;inset:0;background:linear-gradient(180deg,#3d6a3a 0%,#6f9a58 30%,#4fb6e6 55%,#2b98dc 80%,#1b7fcf 100%)}
.topbar{position:absolute;top:0;left:0;width:1200px;height:80px;background:rgba(255,255,255,.95);display:flex;align-items:center}
.brand{position:absolute;left:28px;top:16px;font-family:var(--body);font-size:24px;color:var(--blue-deep);line-height:1.05;width:200px}
.nav{position:absolute;left:290px;top:0;height:80px;display:flex;gap:34px;align-items:center}
.nav a{font-size:15px;color:var(--ink);text-decoration:none;letter-spacing:1px}
.quote-box{position:absolute;right:0;top:0;width:190px;height:96px;background:var(--blue);color:var(--white);text-align:center;padding-top:26px;font-size:15px;line-height:1.5;letter-spacing:1px}
.quote-box strong{font-size:19px;font-weight:400;display:block}
.hero-title{position:absolute;top:320px;width:100%;text-align:center;color:var(--white);font-family:var(--heading);font-size:60px;line-height:1.1;letter-spacing:2px;text-shadow:0 3px 8px rgba(0,0,0,.35)}
.hero-cta{position:absolute;top:460px;left:0;width:100%;text-align:center}
.hero-cta .btn{background:var(--blue)}
.hero-wave{position:absolute;left:0;bottom:0}

/* about */
.about{top:760px;height:560px}
.about-art{position:absolute;left:60px;top:20px;width:460px;height:500px;border-radius:12px;background:radial-gradient(ellipse at 50% 45%,#cfe4f4 0%,#eef5fb 55%,#ffffff 80%)}
.about-copy{position:absolute;left:592px;top:70px;width:560px}
.about-copy p{margin:18px 0 28px}

/* services */
.services{top:1320px;height:640px}
.services-bg{position:absolute;left:0;top:0}
.services .heading{position:absolute;top:90px;width:100%;text-align:center;color:var(--white)}
.cards{position:absolute;top:170px;left:128px;display:flex;gap:20px}
.card{width:224px;height:400px;background:var(--white);border-radius:112px;text-align:center;padding:14px 14px 0;position:relative;box-shadow:0 6px 18px rgba(0,0,0,.15)}
.card .thumb{width:196px;height:196px;border-radius:50%;margin:0 auto}
.card h3{font-family:var(--body);font-size:18px;font-weight:700;margin-top:20px;line-height:1.3}
.card p{font-size:14px;line-height:1.5;margin-top:10px}
.card .plus{position:absolute;bottom:18px;left:0;width:100%;color:var(--blue);font-size:30px}

/* why */
.why{top:2000px;height:700px}
.why-copy{position:absolute;left:128px;top:100px;width:520px}
.why-copy .heading{font-size:54px;line-height:1.1}
.why-copy p{margin:22px 0 26px;font-size:15px}
.feature{position:absolute;width:208px;height:200px;background:var(--white);border-radius:10px;box-shadow:0 4px 18px rgba(0,0,0,.12);text-align:center;padding-top:40px}
.feature svg{display:block;margin:0 auto 18px}
.feature span{font-size:15px;font-weight:700;line-height:1.35;display:block}

/* testimonials */
.testimonials{top:2700px;height:560px}
.test-photo{position:absolute;inset:0;background:linear-gradient(90deg,#1d2a36 0%,#34495a 50%,#4a5e58 100%)}
.test-copy{position:absolute;left:128px;top:110px;width:560px;color:var(--white)}
.test-copy .heading{color:var(--white)}
.test-copy p{color:#e8eef4;margin:16px 0 26px}
.test-name{color:var(--water);font-size:18px}
.test-role{color:#cdd6de;font-size:13px;display:block}
.test-circle{position:absolute;left:720px;top:110px;width:340px;height:340px;border-radius:50%;background:radial-gradient(circle at 50% 45%,#7ad7f5 0%,#36a8e4 60%,#1e7fce 100%);border:6px solid var(--white)}
.dots{position:absolute;top:470px;left:555px;display:flex;gap:10px}
.dots i{width:10px;height:10px;border-radius:50%;background:#9aa7b2}
.dots i.on{background:var(--white)}
.edge{position:absolute;left:0}

/* gallery */
.gallery{top:3260px;height:720px}
.gallery .heading{position:absolute;top:80px;width:100%;text-align:center}
.gallery p{position:absolute;top:158px;left:290px;width:620px;text-align:center;font-size:15px}
.tile{position:absolute;border-radius:6px}

/* contact */
.contact{top:3980px;height:600px}
.contact-bg{position:absolute;left:0;top:0}
.contact .heading{position:absolute;top:150px;width:100%;text-align:center;color:var(--white)}
.contact p{position:absolute;top:222px;left:290px;width:620px;text-align:center;color:#eaf4ff;font-size:15px}
.field{position:absolute;background:var(--white);height:44px;border-radius:3px;font-size:14px;color:#777;padding:12px 16px}
.field.msg{height:140px}
.submit{position:absolute;top:506px;left:525px;width:150px;background:#1b1b1b;color:var(--white);font-size:14px;text-align:center;padding:12px 0;border-radius:24px;letter-spacing:1px}

/* footer */
.footer{top:4580px;height:484px;background:var(--sky)}
.foot-brand{position:absolute;left:120px;top:70px;font-size:26px;color:var(--blue-deep);line-height:1.1;width:220px}
.foot-about{position:absolute;left:120px;top:160px;width:220px;font-size:15px}
.socials{position:absolute;left:120px;top:300px;display:flex;gap:10px}
.socials i{width:36px;height:36px;border:1.5px solid var(--ink);border-radius:50%}
.foot-col{position:absolute;top:80px}
.foot-col h4{font-family:var(--body);font-size:21px;font-weight:700;margin-bottom:18px}
.foot-col li{list-style:none;font-size:14px;color:var(--muted);line-height:2}
.contact-row{display:flex;align-items:center;gap:12px;margin-bottom:18px;font-size:14px;color:var(--muted);line-height:1.35}
.pin{width:38px;height:38px;border-radius:50%;background:var(--blue);flex:none;display:flex;align-items:center;justify-content:center}
.copyright{position:absolute;bottom:0;left:0;width:100%;border-top:1px solid #c9d7e4;text-align:center;font-size:14px;padding:16px 0 20px;color:var(--muted)}
</style>
</head>
<body>

<section class="section hero">
  <div class="hero-photo" role="img" aria-label="Photo of a resort swimming pool surrounded by tropical trees"></div>
  <header class="topbar">
    <div class="brand">Coral Basin<br>Pool Service</div>
    <nav class="nav">
      <a>HOME</a><a>SERVICES</a><a>GALLERY</a><a>ABOUT</a><a>TESTIMONIALS</a><a>CONTACT</a>
    </nav>
  </header>
  <div class="quote-box">GET A FREE QUOTE<strong>123 555 0190</strong></div>
  <h1 class="hero-title">WELCOME TO<br>CORAL BASIN POOL SERVICE</h1>
  <div class="hero-cta"><span class="btn">Get a Free Quote</span></div>
  <svg class="hero-wave" width="1200" height="130" viewBox="0 0 1200 130">
    <path d="M0 40 Q600 150 1200 40 L1200 130 L0 130Z" fill="#ffffff"/>
    <path d="M0 40 Q600 150 1200 40" fill="none" stroke="#2a8fe6" stroke-width="6"/>
  </svg>
</section>

<section class="section about">
  <div class="about-art" role="img" aria-label="Faded photograph of a poolside patio"></div>
  <div class="about-copy">
    <h2 class="heading"><span class="accent">About</span> Us</h2>
    <p>Lorem ipsum dolor sit amet, consectetur adipiscing elit, sed do eiusmod tempor incididunt ut labore et dolore magna aliqua. Quis ipsum suspendisse ultrices gravida. Risus commodo viverra maecenas accumsan lacus vel facilisis. Lorem ipsum dolor sit amet, consectetur adipiscing elit, sed do eiusmod tempor incididunt ut labore et dolore magna aliqua. Quis ipsum suspendisse ultrices gravida. Risus commodo viverra maecenas accumsan lacus vel facilisis.</p>
    <span class="btn">Read More</span>
  </div>
</section>

<section class="section services">
  <svg class="services-bg" width="1200" height="640" viewBox="0 0 1200 640">
    <defs><linearGradient id="svcGrad" x1="0" y1="0" x2="0" y2="1"><stop offset="0" stop-color="#2a8fe6"/><stop offset="1" stop-color="#1464c8"/></linearGradient></defs>
    <path d="M0 40 Q600 -30 1200 40 L1200 590 Q600 660 0 590Z" fill="url(#svcGrad)"/>
  </svg>
  <h2 class="heading">What We Do</h2>
  <div class="cards">
    <div class="card"><div class="thumb" role="img" aria-label="Photo of a clear blue swimming pool" style="background:radial-gradient(circle,#7fd3f2,#2d95d8)"></div><h3>Swimming<br>Pool Services</h3><p>Lorem ipsum dolor<br>consectetur adip.</p><span class="plus">+</span></div>
    <div class="card"><div class="thumb" role="img" aria-label="Photo of a pool being cleaned" style="background:radial-gradient(circle,#9adcf0,#3c8fb8)"></div><h3>Pool Cleaning<br>Service</h3><p>Lorem ipsum dolor<br>consectetur adip.</p><span class="plus">+</span></div>
    <div class="card"><div class="thumb" role="img" aria-label="Photo of a backyard pool at dusk" style="background:radial-gradient(circle,#6cc6e6,#3a6e5a)"></div><h3>Pool Drain &amp;<br>Clean Up</h3><p>Lorem ipsum dolor<br>consectetur adip.</p><span class="plus">+</span></div>
    <div class="card"><div class="thumb" role="img" aria-label="Photo of pool repair work" style="background:radial-gradient(circle,#b9dff0,#4a86b0)"></div><h3>Swimming<br>Pool Repair</h3><p>Lorem ipsum dolor<br>consectetur adip.</p><span class="plus">+</span></div>
  </div>
</section>

<section class="section why">
  <div class="why-copy">
    <h2 class="heading"><span class="accent">Why</span> Choose<br><span class="accent">Coral Basin?</span></h2>
    <p>Lorem ipsum dolor sit amet, consectetur adipiscing elit, sed do eiusmod tempor incididunt ut labore et dolore magna aliqua. Quis ipsum suspendisse ultrices gravida. Risus commodo viverra maecenas accumsan lacus vel facilisis. Lorem ipsum dolor sit amet, consectetur adipiscing elit, sed do eiusmod tempor incididunt ut labore et dolore magna aliqua. Quis ipsum suspendisse ultrices gravida. Risus commodo viverra maecenas accumsan lacus vel facilisis.</p>
    <span class="btn">Read More</span>
  </div>
  <div class="feature" style="left:632px;top:120px">
    <svg width="56" height="56" viewBox="0 0 56 56" fill="none" stroke="#2a8fe6" stroke-width="2.5"><circle cx="28" cy="18" r="10"/><path d="M8 52c0-12 9-20 20-20s20 8 20 20"/><path d="M22 40l5 5 9-9"/></svg>
    <span>Experienced &amp;<br>Professional</span></div>
  <div class="feature" style="left:860px;top:90px">
    <svg width="56" height="56" viewBox="0 0 56 56" fill="none" stroke="#2a8fe6" stroke-width="2.5"><path d="M6 30L30 6h18v18L24 48z"/><circle cx="40" cy="14" r="3"/></svg>
    <span>Competitive<br>Price</span></div>
  <div class="feature" style="left:632px;top:340px">
    <svg width="56" height="56" viewBox="0 0 56 56" fill="none" stroke="#2a8fe6" stroke-width="2.5"><rect x="12" y="6" width="32" height="44" rx="3"/><circle cx="28" cy="26" r="7"/><path d="M24 36l-2 10 6-3 6 3-2-10"/></svg>
    <span>Licensed and<br>Insured</span></div>
  <div class="feature" style="left:860px;top:320px">
    <svg width="56" height="56" viewBox="0 0 56 56" fill="none" stroke="#2a8fe6" stroke-width="2.5"><rect x="10" y="6" width="30" height="42" rx="3"/><path d="M17 18h16M17 26h16M17 34h8"/><path d="M34 44l14-14 4 4-14 14h-4z"/></svg>
    <span>Free<br>Estimates</span></div>
</section>

<section class="section testimonials">
  <div class="test-photo" role="img" aria-label="Dark photograph of a garden waterfall and pool"></div>
  <svg class="edge" style="top:0" width="1200" height="60" viewBox="0 0 1200 60"><path d="M0 0H1200V10Q600 70 0 10Z" fill="#ffffff"/></svg>
  <svg class="edge" style="bottom:0" width="1200" height="70" viewBox="0 0 1200 70"><path d="M0 70H1200V30Q600 -30 0 30Z" fill="#ffffff"/><path d="M0 30Q600 -30 1200 30" fill="none" stroke="#2a8fe6" stroke-width="6"/></svg>
  <div class="test-copy">
    <h2 class="heading">Testimonials</h2>
    <p>Lorem ipsum dolor sit amet, consectetur adipiscing elit, sed do eiusmod tempor incididunt ut labore et dolore magna aliqua. Quis ipsum suspendisse ultrices gravida. Risus commodo viverra maecenas accumsan lacus vel facilisis. Risus commodo viverra maecenas accumsan.</p>
    <span class="test-name">Marisol Dunleavy</span><span class="test-role">Lorem ipsum</span>
  </div>
  <div class="test-circle" role="img" aria-label="Photo of a swimmer relaxing on a yellow float in a pool"></div>
  <div class="dots"><i></i><i class="on"></i><i></i></div>
</section>

<section class="section gallery">
  <h2 class="heading">Our <span class="accent">Gallery</span></h2>
  <p>Lorem ipsum dolor sit amet, consectetur adipiscing elit, sed do eiusmod tempor incididunt ut labore et dolore magna aliqua. Quis ipsum suspendisse ultrices.</p>
  <div class="tile" role="img" aria-label="Photo of a round backyard pool with trees" style="left:72px;top:248px;width:460px;height:400px;background:linear-gradient(180deg,#4f7f3e 0%,#7aa55a 45%,#58bde8 70%,#c9b99a 100%)"></div>
  <div class="tile" role="img" aria-label="Photo of a pool with steps" style="left:548px;top:248px;width:290px;height:192px;background:linear-gradient(160deg,#b8e6f7,#3aa8e0)"></div>
  <div class="tile" role="img" aria-label="Photo of a garden pool" style="left:852px;top:248px;width:280px;height:192px;background:linear-gradient(180deg,#5e8e4a,#4cb8e6)"></div>
  <div class="tile" role="img" aria-label="Photo of friends relaxing in a pool" style="left:548px;top:456px;width:290px;height:192px;background:linear-gradient(180deg,#9cc7d8,#3f9fd2)"></div>
  <div class="tile" role="img" aria-label="Photo of a kidney-shaped pool on a lawn" style="left:852px;top:456px;width:280px;height:192px;background:linear-gradient(180deg,#6a9a4e,#5cc2ea 60%,#7ea85c)"></div>
</section>

<section class="section contact">
  <svg class="contact-bg" width="1200" height="600" viewBox="0 0 1200 600">
    <defs><linearGradient id="ctGrad" x1="0" y1="0" x2="0" y2="1"><stop offset="0" stop-color="#3a9cec"/><stop offset="1" stop-color="#1464c8"/></linearGradient></defs>
    <path d="M0 60 Q600 130 1200 60 L1200 600 L0 600Z" fill="url(#ctGrad)"/>
    <path d="M0 40 Q600 110 1200 40" fill="none" stroke="#2a8fe6" stroke-width="6"/>
  </svg>
  <h2 class="heading">Contact Us</h2>
  <p>Lorem ipsum dolor sit amet, consectetur adipiscing elit, sed do eiusmod tempor incididunt ut labore et dolore magna aliqua. Quis ipsum suspendisse ultrices.</p>
  <div class="field" style="top:300px;left:180px;width:272px">&#128100; Name</div>
  <div class="field" style="top:300px;left:464px;width:272px">&#9993; Email</div>
  <div class="field" style="top:300px;left:748px;width:272px">&#9742; Phone</div>
  <div class="field msg" style="top:356px;left:180px;width:840px">&#9998; Message</div>
  <div class="submit">SUBMIT NOW</div>
</section>

<footer class="section footer">
  <div class="foot-brand">Coral Basin<br>Pool Service</div>
  <p class="foot-about">Lorem ipsum dolor sit amet, consectetur adipiscing elit, ut labore et dolore magna.</p>
  <div class="socials"><i></i><i></i><i></i></div>
  <div class="foot-col" style="left:448px"><h4>Links</h4><ul><li>Home</li><li>Services</li><li>Why Choose Us</li><li>Testimonials</li><li>Contact</li></ul></div>
  <div class="foot-col" style="left:632px"><h4>Service</h4><ul><li>Tile Repair</li><li>Granular Shock</li><li>Pool Cleaning Service</li><li>Pool Repair</li></ul></div>
  <div class="foot-col" style="left:856px"><h4>Contact Us</h4>
    <div class="contact-row"><span class="pin"><svg width="16" height="20" viewBox="0 0 16 20"><path d="M8 0a7 7 0 0 0-7 7c0 5 7 13 7 13s7-8 7-13a7 7 0 0 0-7-7z" fill="#fff"/><circle cx="8" cy="7" r="2.5" fill="#2a8fe6"/></svg></span><span>Location Name<br>Sample Lane,<br>Bayview 00000</span></div>
    <div class="contact-row"><span class="pin"><svg width="18" height="18" viewBox="0 0 18 18"><path d="M4 1l3 4-2 2a10 10 0 0 0 6 6l2-2 4 3-2 3C7 17 1 11 1 3z" fill="#fff"/></svg></span><span>Phone 041 555 0172</span></div>
    <div class="contact-row"><span class="pin"><svg width="18" height="14" viewBox="0 0 18 14"><rect x="1" y="1" width="16" height="12" fill="#fff"/><path d="M1 1l8 6 8-6" fill="none" stroke="#2a8fe6" stroke-width="1.5"/></svg></span><span>info@coralbasin.example</span></div>
  </div>
  <div class="copyright">© 2024 All Rights Reserved Terms &amp; Conditions Privacy Policy</div>
</footer>

</body>
</html>
```